KTR-OB R-Value Adjustment Paper

This is a technical paper needing professional layout that is compatible with our current style guidelines; it will be used in digital and print media. It has numerous tables and graphs.

We have attached a report "KTR Cladding EPD" issued to our company under Marrowfield Assurance graphic design guidelines. While this does NOT reflect our style branding, it does represent the 'technical' presentation we are looking for.

To view our typical company design/style please see our website at www.ktrcouncil.org. Our primary RGB colors are: (187,140,9); (94,47,29); (94,138,164); and (164,167,15). Secondary RGB colors are (249,162,28) and (218,210,208). Our title/header font is DIN Next LT Pro and our copy font is Calibri 10.5 pt. We can deviate from the font specification if beneficial.

The attached file, "KTR-OB Rvalue Adj Factor" is a partial representation of the full document that will need design services. For the concepts we would like to see a cover/title page, a text/copy page and a sample of data graphic treatments.Once we have agreed upon a design concept we will determine full costs to complete the project.

Target Market(s)

Building and construction professionals, architects, building code officials

Font styles to use
Other font styles liked:
• DIN Next LT Pro

Requirements
Must have
• Design elements that help make the information easy to read and use.
Nice to have
• Right amount of white space.

```html
<!DOCTYPE html>
<html lang="en">
<head>
<meta charset="utf-8">
<title>KTR-OB R-Value Adjustment Paper – Concept Pages</title>
<link rel="stylesheet" href="https://fonts.googleapis.com/css2?family=Barlow+Semi+Condensed:wght@500;600;700&family=Carlito:wght@400;700&display=swap">
<style>
  :root{
    --gold:#bb8c09;
    --brown:#5e2f1d;
    --blue:#5e8aa4;
    --green:#a4a70f;
    --orange:#f9a21c;
    --stone:#dad2d0;
    --ink:#3a3a3a;
    --canvas:#ececec;
    --badge:#8cc63f;
    --head:"Barlow Semi Condensed", "DIN Next LT Pro", sans-serif;
    --copy:"Carlito", Calibri, sans-serif;
  }
  *{box-sizing:border-box;margin:0;padding:0}
  html,body{width:1200px;height:964px;overflow:hidden;background:var(--canvas)}
  body{position:relative;font-family:var(--copy);color:var(--ink)}

  .page{position:absolute;background:#fff;box-shadow:0 2px 10px rgba(0,0,0,.18);overflow:hidden}

  /* ---------- Cover ---------- */
  .cover{left:146px;top:86px;width:560px;height:792px}
  .cover__topband{position:absolute;left:0;top:0;width:100%;height:8px;background:var(--brown)}
  .brand{display:flex;align-items:center;gap:6px;font-family:var(--head);font-weight:600;color:var(--gold)}
  .brand__dot{border-radius:50%;background:var(--gold);flex:none}
  .cover .brand{position:absolute;left:50%;top:76px;transform:translateX(-50%);font-size:22px;letter-spacing:.5px}
  .cover .brand__dot{width:22px;height:22px}
  .cover__title{position:absolute;left:40px;right:40px;top:150px;text-align:center;font-family:var(--head);font-weight:600;font-size:23px;line-height:1.15;color:var(--brown)}
  .rule{position:absolute;left:0;width:100%;height:3px;background:linear-gradient(90deg,var(--brown) 0%,var(--gold) 40%,var(--green) 65%,var(--blue) 100%)}
  .cover .rule{top:280px}
  .cover__photo{position:absolute;left:0;top:283px;width:100%;height:480px;background:linear-gradient(135deg,#7d776b 0%,#a6a196 35%,#e6e6e4 60%,#f7f7f5 100%)}
  .cover__wave{position:absolute;left:0;top:283px}
  .cover__date{position:absolute;left:56px;top:690px;font-size:12px;color:#fff}
  .cover__badge{position:absolute;left:430px;top:640px;width:64px;height:76px;border-radius:8px;background:var(--badge)}
  .cover__footband{position:absolute;left:0;bottom:0;width:100%;height:28px;background:var(--brown);color:#fff;font-size:7.5px;letter-spacing:.3px;text-align:center;line-height:28px}

  /* ---------- Inner pages ---------- */
  .inner{left:746px;width:308px;height:436px}
  .inner--data{top:40px}
  .inner--text{top:488px}
  .inner .rule{top:42px;height:2px}
  .inner .brand{position:absolute;right:14px;top:14px;font-size:9px}
  .inner .brand__dot{width:11px;height:11px}
  .inner__heading{position:absolute;left:32px;font-family:var(--head);font-weight:700;font-size:9.5px;color:var(--ink)}
  .copy{position:absolute;left:32px;right:40px;font-size:5px;line-height:1.75;color:#555}
  .caption{position:absolute;left:0;width:100%;text-align:center;font-size:3.6px;font-style:italic;color:#888}
  .inner__footer{position:absolute;left:16px;right:16px;top:412px;border-top:.6px solid #ccc;text-align:center;font-size:4.2px;color:#555;padding-top:6px}
  .inner__footer::before{content:"";position:absolute;left:50%;top:-1.5px;width:40px;margin-left:-20px;height:2px;background:linear-gradient(90deg,var(--brown),var(--gold),var(--green))}

  /* table */
  .rtable{position:absolute;left:32px;top:120px;width:196px;border-collapse:collapse;font-size:3.8px;color:#444}
  .rtable th{background:var(--gold);color:#fff;font-weight:400;text-align:left;padding:2px 3px}
  .rtable td{padding:2.2px 3px;border-bottom:.5px solid #e2d7b8}
  .rtable td:first-child{color:#333}

  /* chart */
  .chart{position:absolute;left:0;top:234px;width:308px;height:172px;background:#f4f4f4}
  .chart text{font-family:var(--copy)}

  /* summary bullets */
  .points{position:absolute;left:32px;right:36px;top:208px;list-style:none}
  .points li{position:relative;background:#eeeeee;border-bottom:1px solid #fff;padding:4px 6px 4px 12px;font-size:4.6px;line-height:1.6;color:#555}
  .points li::before{content:"";position:absolute;left:4px;top:9px;width:2px;height:2px;border-radius:50%;background:#333}
</style>
</head>
<body>

<!-- Cover page -->
<section class="page cover">
  <div class="cover__topband"></div>
  <div class="brand"><span class="brand__dot"></span>KTR-OB</div>
  <h1 class="cover__title">Polystyrene Foam Insulation in Long-Term<br>Building Applications – Effective R-values</h1>
  <div class="rule"></div>
  <div class="cover__photo" role="img" aria-label="Construction worker in a hard hat fitting white foam insulation boards onto a concrete wall"></div>
  <svg class="cover__wave" width="560" height="480" viewBox="0 0 560 480" aria-hidden="true">
    <path d="M0 360 C 150 345, 230 260, 330 235 C 430 210, 500 230, 560 280 L560 480 L0 480 Z" fill="var(--gold)"/>
  </svg>
  <p class="cover__date">August 2018</p>
  <div class="cover__badge" aria-hidden="true"></div>
  <footer class="cover__footband">DRAFT – NOT FOR DISTRIBUTION Intended for KTR-OB Committee Discussion Purposes Only</footer>
</section>

<!-- Data page -->
<section class="page inner inner--data">
  <div class="brand"><span class="brand__dot"></span>KTR-OB</div>
  <div class="rule"></div>
  <h2 class="inner__heading" style="top:60px">Temperature Adjustment Factor</h2>
  <p class="copy" style="top:77px">The performance of polystyrene foam insulation is well documented in ASTM C578 (ASTM, 2017). The R-value performance of both EPS and XPS increases at mean temperatures colder than 75 °F and decreases at mean temperatures warmer than 75 °F. The table below provides the recognized R-values at 75 °F for polystyrene in compliance with ASTM C578 as well as the R-values at 110, 40, and 25 °F mean temperatures.</p>
  <table class="rtable">
    <tr><th>Material</th><th>EPS</th><th>EPS</th><th>XPS</th><th>XPS</th></tr>
    <tr><td>ASTM C578 Type</td><td>II</td><td>IX</td><td>X</td><td>IV</td></tr>
    <tr><td>R-value at 110 °F</td><td>3.65</td><td>3.85</td><td>4.65</td><td>4.65</td></tr>
    <tr><td>R-value at 75 °F</td><td>4.0</td><td>4.2</td><td>5.0</td><td>5.0</td></tr>
    <tr><td>R-value at 40 °F</td><td>4.4</td><td>4.6</td><td>5.4</td><td>5.4</td></tr>
    <tr><td>R-value at 25 °F</td><td>4.6</td><td>4.8</td><td>5.6</td><td>5.6</td></tr>
  </table>
  <p class="caption" style="top:197px;left:-20px">Table 3: ASTM C578 R-values at Various Mean Temperatures</p>
  <p class="copy" style="top:206px">Plotting the various R-values in ASTM C578 in Figure 5 shows that there is a linear relationship of R-value with temperature that allows the R-value to be predicted at any mean temperature within the range of 25 to 110 °F.</p>
  <svg class="chart" viewBox="0 0 308 172" role="img" aria-label="Line chart of R-value versus mean temperature for EPS Type II, EPS Type IX and EPS Type IV and X">
    <g stroke="#bbb" stroke-width=".5" stroke-dasharray="1.5 1.5">
      <line x1="45" y1="15" x2="270" y2="15"/><line x1="45" y1="32.5" x2="270" y2="32.5"/>
      <line x1="45" y1="50" x2="270" y2="50"/><line x1="45" y1="67.5" x2="270" y2="67.5"/>
      <line x1="45" y1="85" x2="270" y2="85"/><line x1="45" y1="102.5" x2="270" y2="102.5"/>
      <line x1="82.5" y1="15" x2="82.5" y2="120"/><line x1="120" y1="15" x2="120" y2="120"/>
      <line x1="157.5" y1="15" x2="157.5" y2="120"/><line x1="195" y1="15" x2="195" y2="120"/>
      <line x1="232.5" y1="15" x2="232.5" y2="120"/><line x1="270" y1="15" x2="270" y2="120"/>
    </g>
    <line x1="45" y1="120" x2="270" y2="120" stroke="#999" stroke-width=".6"/>
    <g font-size="4.5" fill="#333" text-anchor="end">
      <text x="40" y="16.5">6</text><text x="40" y="34">5.5</text><text x="40" y="51.5">5</text>
      <text x="40" y="69">4.5</text><text x="40" y="86.5">4</text><text x="40" y="104">3.5</text><text x="40" y="121.5">3</text>
    </g>
    <g font-size="4.5" fill="#333" text-anchor="middle">
      <text x="45" y="128">10</text><text x="82.5" y="128">30</text><text x="120" y="128">50</text>
      <text x="157.5" y="128">70</text><text x="195" y="128">90</text><text x="232.5" y="128">110</text><text x="270" y="128">130</text>
    </g>
    <g stroke-width="1" fill="none">
      <line x1="66" y1="26" x2="245" y2="67" stroke="#111"/>
      <line x1="66" y1="56" x2="245" y2="96.5" stroke="var(--orange)"/>
      <line x1="66" y1="61" x2="245" y2="103.5" stroke="var(--green)"/>
    </g>
    <g fill="#111"><circle cx="73.1" cy="29" r="1.5"/><circle cx="101.25" cy="36" r="1.5"/><circle cx="166.9" cy="50" r="1.5"/><circle cx="232.5" cy="62.25" r="1.5"/></g>
    <g fill="var(--orange)"><circle cx="73.1" cy="59" r="1.5"/><circle cx="101.25" cy="66" r="1.5"/><circle cx="166.9" cy="80" r="1.5"/><circle cx="232.5" cy="92.25" r="1.5"/></g>
    <g fill="var(--green)"><circle cx="73.1" cy="64" r="1.5"/><circle cx="101.25" cy="71" r="1.5"/><circle cx="166.9" cy="85" r="1.5"/><circle cx="232.5" cy="99.25" r="1.5"/></g>
    <g font-size="4" fill="#333">
      <rect x="83" y="140" width="8" height="2" fill="var(--green)"/><text x="94" y="142.5">EPS Type II</text>
      <rect x="135" y="140" width="8" height="2" fill="var(--orange)"/><text x="146" y="142.5">EPS Type IX</text>
      <rect x="190" y="140" width="8" height="2" fill="#111"/><text x="201" y="142.5">EPS Type IV and X</text>
    </g>
    <text x="154" y="160" font-size="3.6" fill="#888" font-style="italic" text-anchor="middle">Figure 5. R-value vs. Mean Temperature for Type II, IX, IV, and X Polystyrene Insulation</text>
  </svg>
  <footer class="inner__footer">Polystyrene Foam Insulation in Long-Term Building Applications – Effective R-values</footer>
</section>

<!-- Text page -->
<section class="page inner inner--text">
  <div class="brand"><span class="brand__dot"></span>KTR-OB</div>
  <div class="rule"></div>
  <h2 class="inner__heading" style="top:74px">Executive Summary</h2>
  <p class="copy" style="top:111px">The primary purpose of insulation is to isolate a building's interior environment from either warm or cold exterior conditions. In many building applications, polystyrene foam insulation is protected from moisture, and the R-values determined under dry laboratory conditions are appropriate. This document provides a methodology that uses short-term, laboratory-determined R-values with adjustment factors to account for the long-term conditions of buildings when a more detailed analysis is desired. The focus is on the insulation R-value performance of expanded polystyrene (EPS) and extruded polystyrene (XPS) foam products used in long-term building applications. The laboratory-determined R-value is multiplied by three adjustment factors to determine the long-term effective R-value of installed insulation. After considering the impact of temperature, age, and moisture on both EPS and XPS, the following conclusions are drawn:</p>
  <ul class="points">
    <li>The R-values for EPS and XPS increase when the mean temperature decreases below 75 °F. At a mean temperature of 40 °F, the R-values for EPS and XPS increase by approximately 10%.</li>
    <li>The R-value for EPS was constant over time, and the R-value for XPS decreased by approximately 14% over time.</li>
    <li>The R-values for both EPS and XPS is approximated to decrease by 10% due to the absorption of water in below grade applications.</li>
  </ul>
  <p class="copy" style="top:286px">The magnitudes of the adjustments to the R-values were not extremely large, but the analysis demonstrated that the R-value performance of EPS was preserved better than that of XPS when all factors were considered. The prime contributor to this difference was the loss of R-value by XPS that occurred with age.</p>
  <footer class="inner__footer">Polystyrene Foam Insulation in Long-Term Building Applications – Effective R-values</footer>
</section>

</body>
</html>
```